Wren Renovation Collective Postcard Design Project

I'm a General Contractor specializing in luxury residential remodeling.

THIS IS AN EDDM POSTCARD. THE ENTIRE BACK SIDE OF THE CARD WILL BE USED.

I FORGOT TO MENTION THIS IN MY ORIGINAL BRIEF.

Target Market(s)

OLD, rich people so please make sure the fonts are clear and crisp.

Font styles to use
Sans Serif

```html
<!DOCTYPE html>
<html lang="en">
<head>
<meta charset="utf-8">
<title>Wren Renovation Collective – Postcard Back</title>
<link href="https://fonts.googleapis.com/css2?family=Lato:wght@400;700;900&display=swap" rel="stylesheet">
<style>
  :root {
    --page-bg: #d8d8db;
    --card-bg: #eeecea;
    --brand-red: #d62126;
    --brand-red-dark: #b5181d;
    --ink: #111111;
    --white: #ffffff;
    --icon-blue: #1e9be0;
    --ring-blue: #8fd0f2;
    --pill-light: #5ec3e6;
    --pill-dark: #1452a8;
    --photo-border: #3a3a3a;
  }
  * { box-sizing: border-box; margin: 0; padding: 0; }
  html, body { width: 1200px; height: 1200px; overflow: hidden; }
  body { background: var(--page-bg); font-family: "Lato", Arial, sans-serif; position: relative; }

  .postcard {
    position: absolute; left: 0; top: 195px; width: 1200px; height: 810px;
    background: radial-gradient(ellipse at 50% 50%, #fbfbfa 0%, #ecebe9 70%, #e2e0de 100%);
    overflow: hidden;
  }
  .blueprint-field {
    position: absolute; inset: 0;
    background: linear-gradient(160deg, rgba(200,200,205,.25), rgba(255,255,255,0) 40%, rgba(200,200,205,.25));
  }

  .headline-band {
    position: absolute; left: 0; top: 60px; width: 100%; height: 85px;
    background: linear-gradient(180deg, var(--brand-red) 0%, var(--brand-red-dark) 100%);
    border-bottom: 7px solid var(--ink);
    box-sizing: content-box;
    display: flex; align-items: center; justify-content: center;
  }
  .headline {
    color: var(--white); font-weight: 900; font-size: 31px; line-height: 39px;
    text-align: center; letter-spacing: .2px;
  }

  .photo {
    position: absolute; top: 218px; width: 362px; height: 374px;
    border: 4px solid var(--photo-border); box-shadow: 2px 3px 6px rgba(0,0,0,.35);
  }
  .photo--interior { left: 38px; background: linear-gradient(180deg, #d8d2c4 0%, #a58a66 55%, #6b4a2c 100%); }
  .photo--exterior { left: 798px; background: linear-gradient(180deg, #b9c4b0 0%, #c9b98f 40%, #6fa33a 70%, #4f8a26 100%); }

  .values-graphic { position: absolute; left: 0; top: 0; }

  .value { position: absolute; width: 150px; text-align: center; font-weight: 700; font-size: 15px; line-height: 19px; color: var(--ink); }
  .value-icon { display: block; width: 40px; height: 40px; margin: 0 auto 2px; }

  .brand-mark {
    position: absolute; left: 520px; top: 340px; width: 140px; text-align: center;
    color: var(--brand-red); font-weight: 900; font-size: 17px; line-height: 19px;
  }
  .core-title {
    position: absolute; left: 515px; top: 380px; width: 150px; text-align: center;
    font-weight: 900; font-size: 28px; line-height: 33px; color: var(--ink);
  }

  .contact-band {
    position: absolute; left: 0; top: 650px; width: 100%; height: 118px;
    background: var(--ink); border-bottom: 12px solid var(--brand-red); box-sizing: content-box;
  }
  .contractor-name { position: absolute; left: 86px; top: 26px; color: var(--white); font-weight: 700; font-size: 39px; line-height: 44px; }
  .contractor-role { position: absolute; left: 86px; top: 67px; color: var(--white); font-size: 20px; line-height: 24px; }

  .contact-pill {
    position: absolute; right: 0; top: 24px; width: 438px; height: 78px;
    border-radius: 39px 0 0 39px;
    background: linear-gradient(90deg, var(--pill-light) 0%, #2f86cc 55%, var(--pill-dark) 100%);
    padding: 10px 0 0 46px; color: var(--white); font-size: 20px; line-height: 26px;
  }
  .contact-line { display: flex; align-items: center; gap: 9px; white-space: nowrap; }
  .contact-line svg { width: 17px; height: 17px; flex: none; }
  .contact-web { font-size: 18px; }
</style>
</head>
<body>
  <section class="postcard">
    <div class="blueprint-field" role="img" aria-label="Faint architectural blueprint lines in the background"></div>

    <header class="headline-band">
      <h1 class="headline">REMODELING LUXURY HOMES &amp; BUILDING LASTING<br>RELATIONSHIPS SINCE 1995</h1>
    </header>

    <div class="photo photo--interior" role="img" aria-label="Photo of a bright remodeled dining nook with a round wooden table and chairs"></div>
    <div class="photo photo--exterior" role="img" aria-label="Photo of a luxury craftsman-style home with a manicured green lawn"></div>

    <svg class="values-graphic" width="1200" height="810" viewBox="0 0 1200 810" aria-hidden="true">
      <g fill="none" stroke="var(--ring-blue)">
        <circle cx="590" cy="398" r="158" stroke-width="3" opacity=".7"/>
        <circle cx="590" cy="398" r="146" stroke-width="1.5" opacity=".6"/>
        <circle cx="590" cy="398" r="100" stroke-width="6" opacity=".55" stroke-dasharray="120 14"/>
        <circle cx="590" cy="398" r="88" stroke-width="2" opacity=".7"/>
        <circle cx="590" cy="398" r="80" stroke-width="1" opacity=".6"/>
      </g>
      <circle cx="590" cy="398" r="76" fill="#ffffff" opacity=".85"/>
    </svg>

    <div class="brand-mark">Wren Renovation Collective</div>
    <div class="core-title">CORE<br>VALUES</div>

    <div class="value" style="left:515px; top:214px;">
      <svg class="value-icon" viewBox="0 0 40 40"><rect width="40" height="40" rx="6" fill="var(--icon-blue)"/><g fill="#fff"><circle cx="20" cy="12" r="4"/><circle cx="11" cy="22" r="3"/><circle cx="29" cy="22" r="3"/><rect x="15" y="17" width="10" height="9" rx="3"/><rect x="7" y="26" width="8" height="7" rx="2"/><rect x="25" y="26" width="8" height="7" rx="2"/></g></svg>
      Educating Our<br>Clients
    </div>
    <div class="value" style="left:393px; top:292px;">
      <svg class="value-icon" viewBox="0 0 40 40"><rect width="40" height="40" rx="6" fill="var(--icon-blue)"/><circle cx="20" cy="16" r="8" fill="#fff"/><rect x="16" y="23" width="8" height="8" rx="2" fill="#fff"/></svg>
      The Creative<br>Process
    </div>
    <div class="value" style="left:637px; top:292px;">
      <svg class="value-icon" viewBox="0 0 40 40"><rect width="40" height="40" rx="6" fill="var(--icon-blue)"/><circle cx="24" cy="14" r="6" fill="#ffd23f"/><path d="M6 28c6-5 12-5 18-2l8-4v6l-10 5H8z" fill="#fff"/></svg>
      Quality<br>Craftsmanship
    </div>
    <div class="value" style="left:393px; top:437px;">
      <svg class="value-icon" viewBox="0 0 40 40"><rect width="40" height="40" rx="6" fill="var(--icon-blue)"/><path d="M20 6l12 5v9c0 8-6 12-12 14C14 32 8 28 8 20v-9z" fill="#fff"/><path d="M14 20l5 5 9-10" fill="none" stroke="#f2b705" stroke-width="3.5" stroke-linecap="round"/></svg>
      Integrity
    </div>
    <div class="value" style="left:643px; top:437px;">
      <svg class="value-icon" viewBox="0 0 40 40"><rect width="40" height="40" rx="6" fill="var(--icon-blue)"/><path d="M6 18l8-6 6 4 6-4 8 6-12 10z" fill="#fff"/></svg>
      World Class<br>Customer Service
    </div>
    <div class="value" style="left:516px; top:525px;">
      <svg class="value-icon" viewBox="0 0 40 40"><rect width="40" height="40" rx="6" fill="var(--icon-blue)"/><circle cx="20" cy="21" r="12" fill="#fff"/><circle cx="20" cy="21" r="8" fill="var(--icon-blue)"/><circle cx="20" cy="21" r="4" fill="#fff"/><path d="M20 21L32 9" stroke="var(--brand-red)" stroke-width="2.5"/></svg>
      Having Fun
    </div>

    <footer class="contact-band">
      <div class="contractor-name">Daniel Wren</div>
      <div class="contractor-role">General Contractor</div>
      <div class="contact-pill">
        <div class="contact-line contact-web">
          <svg viewBox="0 0 20 20"><path d="M5 2l3 4-2 2c1 2 3 4 5 5l2-2 4 3-2 3c-6 0-12-6-13-13z" fill="#fff"/></svg>
          www.WrenRenovationCollective.com
        </div>
        <div class="contact-line">
          <svg viewBox="0 0 20 20"><circle cx="10" cy="10" r="8" fill="#fff"/><path d="M6 6c2 1 3 3 2 5s1 3 3 3M12 4c0 2 2 3 4 3" stroke="#2f86cc" stroke-width="1.6" fill="none"/></svg>
          480-555-0142
        </div>
      </div>
    </footer>
  </section>
</body>
</html>
```